Photojournalism/photography business needs a simple, timeless & professional letterhead design

We need a letterhead design for photography/photojournalism business called 'qolvb', no capitals.

The letterhead needs to be:
- simple
- professional
- timeless
- easy to read
- consists of at least 2 colors to make it stands out.

We do mainly editorial photography, photo articles for various publications, travel, businesses, as well as people such as family and kids.

The final design should communicate professionalism, easy identification, attention grabbing, even if it has to be found among a stack of various papers on the clients' desks.

Target Market(s)

Various publications.

Industry/Entity Type

Business

Requirements
Must have
• Please use the logo attached.

```html
<!DOCTYPE html>
<html lang="en">
<head>
<meta charset="utf-8">
<title>qolvb letterhead</title>
<link href="https://fonts.googleapis.com/css2?family=Nunito:wght@400;800&display=swap" rel="stylesheet">
<style>
  :root {
    --backdrop: #e6e4e1;
    --paper: #ffffff;
    --paper-tint: #f3f3f3;
    --ink: #3d3d3d;
    --ink-soft: #6b6b6b;
    --accent: #b5532a;
    --paper-edge: #d9d9d9;
  }
  html, body {
    margin: 0;
    padding: 0;
    width: 1200px;
    height: 1181px;
    overflow: hidden;
    background: var(--backdrop);
  }
  .letterhead {
    position: absolute;
    left: 284px;
    top: 133px;
    width: 634px;
    height: 904px;
    background: radial-gradient(circle at 50% 50%, var(--paper) 30%, var(--paper-tint) 100%);
    box-shadow: 0 0 0 1px var(--paper-edge);
    font-family: "Nunito", sans-serif;
  }
  .letterhead__brand {
    position: absolute;
    top: 18px;
    left: 0;
    right: 0;
    text-align: center;
    font-weight: 800;
    font-size: 84px;
    line-height: 1;
    letter-spacing: -1px;
    color: var(--ink);
  }
  .letterhead__rule {
    position: absolute;
    top: 116px;
    left: 222px;
    width: 190px;
    height: 3px;
    background: var(--accent);
  }
  .letterhead__footer {
    position: absolute;
    left: 0;
    right: 0;
    bottom: 26px;
    height: 96px;
  }
  .letterhead__footer-mark {
    position: absolute;
    left: 50%;
    top: 0;
    width: 88px;
    height: 88px;
    margin-left: -44px;
    background: var(--accent);
  }
  .letterhead__contact {
    position: absolute;
    top: 30px;
    width: 230px;
    font-size: 13px;
    line-height: 18px;
    color: var(--ink-soft);
  }
  .letterhead__contact--left {
    left: 30px;
    text-align: right;
  }
  .letterhead__contact--right {
    right: 30px;
    text-align: left;
  }
</style>
</head>
<body>
  <main class="letterhead">
    <div class="letterhead__brand">qolvb</div>
    <div class="letterhead__rule"></div>
    <footer class="letterhead__footer">
      <div class="letterhead__contact letterhead__contact--left">
        14 Harbour Lane, Westmoor<br>+1 555 0147 822
      </div>
      <div class="letterhead__footer-mark"></div>
      <div class="letterhead__contact letterhead__contact--right">
        studio@qolvb.com<br>www.qolvb.com
      </div>
    </footer>
  </main>
</body>
</html>
```